Top notch designer needed for world class recruitment app!

We need an app design for an Amsterdam-based company that is about to change the way we find new jobs. The idea is not to show the company and job title as everyone does, but only a 5 sentence summary of the job. The user slides though the jobs and eventuelly finds a shortlist of his best matching jobs.

Winning designers supplies 2 designs, that have contain the core of our business idea (see screenshots attached):

Screenshot 1, A job description done in 5 bulletpoints (6-9 words).

example:

- Lead 20 enthusiastic workers
- Coordinate between production department and development team
- Improve current processes
- Maintain relations with supplier
- Lot of focus on personal development

Screenshot 2 should be a shortlist/favourites

The shortlists shows around 5 jobs with job title, company logo, number of days the
vacancy will stay available, and how well the job matches to your profile (preferably by means of a visual indicator).

Target Market(s)

Young professionals looking for a job. Well educated withless than 10 years work experience. Typical user would be someone who uses workvine regularly.

Industry/Entity Type

Business

Requirements
Must have
• The 2 screenshots (see attachment) with awesome look and feel, with content as described in attachment.. The winning designs should (also) be available in PSD format, or less preferably in PNG.

Nice to have
• Inspiration:
Flicko: simple and clear slide throughs (yes/no)
Workvine: start screen (professional and stylish), vacancy banner (visual, but not distracting)
Roomly: combination of playfull and professional design
Should not have
• We like to have it as visual as possible, but visuals cannot directly relate to the job (because we cannot match a visual to every job). So should be something 'business like' or 'city life'.

When a user clicks on the 'i (more info)' button the user can see info like job title, company name, location. Its important that this info is not shown in screenshot 1.

```html
<!DOCTYPE html>
<html lang="en">
<head>
<meta charset="utf-8">
<title>Find Me – Job Card</title>
<link rel="stylesheet" href="https://fonts.googleapis.com/css2?family=Open+Sans:wght@700&family=Quicksand:wght@400&display=swap">
<style>
  :root {
    --page-bg: #ececec;
    --frame: #111111;
    --screen-bg: #f3f1ed;
    --green-top: #6cc644;
    --green-bottom: #1c9a1c;
    --bullet-green: #3fae2a;
    --card-top: #ffffff;
    --card-bottom: #f1efec;
    --card-border: #d9d7d3;
    --text-dark: #2e2e2e;
    --white: #ffffff;
    --nope-red: #ec5a44;
    --info-blue: #4aa6dd;
    --like-green: #5fd14a;
    --ring: #f7f7f7;
    --ring-border: #e2e2e2;
  }
  * { box-sizing: border-box; margin: 0; padding: 0; }
  html, body { width: 1200px; height: 1000px; overflow: hidden; }
  body { background: var(--page-bg); position: relative; }

  .app-screen {
    position: absolute; left: 325px; top: 68px; width: 577px; height: 858px;
    border: 8px solid var(--frame); border-radius: 5px;
    background: var(--screen-bg); overflow: hidden;
  }
  .app-header {
    position: absolute; left: 0; top: 0; width: 100%; height: 110px;
    background: linear-gradient(var(--green-top), var(--green-bottom));
  }
  .menu-button {
    position: absolute; left: 34px; top: 17px; width: 78px; height: 78px;
    border-radius: 6px; background: rgba(0,0,0,0.08);
    border: 1px solid rgba(0,0,0,0.12);
    display: flex; flex-direction: column; justify-content: center; gap: 9px; padding: 0 9px;
  }
  .menu-button span { display: block; height: 4px; background: rgba(255,255,255,0.85); border-radius: 1px; }
  .app-title {
    position: absolute; left: 0; right: 26px; top: 30px; text-align: center;
    font-family: "Open Sans", sans-serif; font-weight: 700; font-size: 40px;
    color: var(--white); letter-spacing: 0.5px; line-height: 52px;
  }
  .profile-avatar {
    position: absolute; left: 436px; top: 17px; width: 79px; height: 79px;
    border-radius: 6px;
    background: linear-gradient(#8aa0b6 0%, #c9d2d8 45%, #7b9a5a 100%);
    border: 2px solid var(--white);
  }

  .job-summary { position: absolute; left: 15px; top: 137px; width: 530px; list-style: none; }
  .summary-point {
    position: absolute; left: 0; width: 530px;
    background: linear-gradient(var(--card-top) 40%, var(--card-bottom));
    border: 1px solid var(--card-border); border-radius: 13px;
    display: flex; align-items: center;
  }
  .summary-point .bullet {
    position: absolute; left: 19px; width: 45px; height: 45px; border-radius: 6px;
    background: var(--bullet-green);
  }
  .summary-point .bullet svg { position: absolute; left: 15px; top: 13px; }
  .summary-point p {
    margin-left: 80px; font-family: "Quicksand", sans-serif; font-weight: 400;
    font-size: 29px; line-height: 44px; color: var(--text-dark);
    letter-spacing: -0.4px; white-space: nowrap;
  }

  .swipe-actions { position: absolute; left: 0; top: 672px; width: 100%; height: 170px; }
  .action { position: absolute; border-radius: 50%; background: var(--ring); border: 1px solid var(--ring-border); }
  .action .face {
    position: absolute; border-radius: 50%;
    background: linear-gradient(#fdfdfd, #e6e6e6);
    border: 1px solid #d6d6d6; box-shadow: 0 2px 3px rgba(0,0,0,0.12);
    display: flex; align-items: center; justify-content: center;
  }
  .action-nope { left: 75px; top: 2px; width: 156px; height: 156px; }
  .action-like { left: 334px; top: 2px; width: 156px; height: 156px; }
  .action-nope .face, .action-like .face { left: 24px; top: 24px; width: 108px; height: 108px; }
  .action-info { left: 221px; top: 22px; width: 116px; height: 116px; }
  .action-info .face { left: 18px; top: 18px; width: 80px; height: 80px; }
  .info-glyph { font-family: Georgia, serif; font-style: italic; font-weight: 700; font-size: 34px; color: var(--info-blue); }
</style>
</head>
<body>
  <main class="app-screen">
    <header class="app-header">
      <div class="menu-button"><span></span><span></span><span></span><span></span><span></span></div>
      <h1 class="app-title">FIND ME</h1>
      <div class="profile-avatar" role="img" aria-label="User profile photo"></div>
    </header>

    <ul class="job-summary">
      <li class="summary-point" style="top:0;height:78px;">
        <span class="bullet"><svg width="16" height="19" viewBox="0 0 16 19"><path d="M1 1 L15 9.5 L1 18 Z" fill="#fff"/></svg></span>
        <p>Lead 20 enthusiatic workers</p>
      </li>
      <li class="summary-point" style="top:88px;height:112px;">
        <span class="bullet"><svg width="16" height="19" viewBox="0 0 16 19"><path d="M1 1 L15 9.5 L1 18 Z" fill="#fff"/></svg></span>
        <p>Coordinate between production<br>deparment and developmnt team</p>
      </li>
      <li class="summary-point" style="top:221px;height:78px;">
        <span class="bullet"><svg width="16" height="19" viewBox="0 0 16 19"><path d="M1 1 L15 9.5 L1 18 Z" fill="#fff"/></svg></span>
        <p>Improve current processes</p>
      </li>
      <li class="summary-point" style="top:310px;height:78px;">
        <span class="bullet"><svg width="16" height="19" viewBox="0 0 16 19"><path d="M1 1 L15 9.5 L1 18 Z" fill="#fff"/></svg></span>
        <p>Maintain relations with</p>
      </li>
      <li class="summary-point" style="top:400px;height:112px;">
        <span class="bullet"><svg width="16" height="19" viewBox="0 0 16 19"><path d="M1 1 L15 9.5 L1 18 Z" fill="#fff"/></svg></span>
        <p>Lot of focus on personal<br>development</p>
      </li>
    </ul>

    <nav class="swipe-actions">
      <div class="action action-nope"><div class="face">
        <svg width="54" height="54" viewBox="0 0 54 54"><path d="M8 14 L14 8 L27 21 L40 8 L46 14 L33 27 L46 40 L40 46 L27 33 L14 46 L8 40 L21 27 Z" fill="var(--nope-red)"/></svg>
      </div></div>
      <div class="action action-like"><div class="face">
        <svg width="62" height="54" viewBox="0 0 62 54"><path d="M31 52 C12 36 2 27 2 15 C2 7 8 1 16 1 C23 1 28 5 31 10 C34 5 39 1 46 1 C54 1 60 7 60 15 C60 27 50 36 31 52 Z" fill="var(--like-green)"/></svg>
      </div></div>
      <div class="action action-info"><div class="face"><span class="info-glyph">i</span></div></div>
    </nav>
  </main>
</body>
</html>
```